Dog themed post card for homeowners that may be willing to sell their house.

We will be sending these postcards to homeowners that may be interested in selling their house. Our business is themed around our dog "Wexley"- Wexley Buys Houses. We are using her as the focal point of the business because typically these homeowners get lots of mailers that are similar and we would like stand out with an inviting puppy dog.
We would like to included the icon for facebook and instragam with her handle "@WexleyBuysHouses" and her website WexleyBuysHouses.example and our phone number 555-814-2760.
We will be sending these postcards in batches to various subdivisions. For that reason please consider a format that can easily change the name of the subdivision. We are including the subdivision name because we want the postcard to be slightly more personal/targeted.
Our business is just starting and we would like to get some brand recognition going. We envision Wexley Buys Houses predominately displayed somehow.
I have attached numerous pictures of Wexley. We envision using one on each side of the postcard. Below are phrases we would like to include on the postcard in a format that you see fitting. Please use the verbiage below and not what is sketched on the uploaded postcard. The below verbiage is the most up to date.
-I recently bought a house in (subdivision name) and would love to buy yours.
-Call my humans today so we can give you a no obligation offer
-No money out of your pocket
-Quick closing
-Any condition
-Can help with moving expenses

Target Market(s)

Home owners with equity in their house that may need to sell quickly. These are generally people that do not enjoy the buying/selling of real estate. It can sometimes be someone who has recently inherited a home and doesnt want to deal with the headache. Other times it may be someone going through a divorce or forclosure and want to sell their home quickly.

Industry/Entity Type

Direct Marketing

Requirements
Must have
• Happy and bright feel. This industry is saturated with less than ethical people and we are trying to convey a very clean, honest, straight forward and scam-free process.

```html
<!DOCTYPE html>
<html lang="en">
<head>
<meta charset="utf-8">
<title>Wexley Buys Houses – Postcard</title>
<link rel="stylesheet" href="https://fonts.googleapis.com/css2?family=Bebas+Neue&family=Montserrat:wght@500;600;700;800&display=swap">
<style>
  :root {
    --brand-blue: #0a6896;
    --brand-yellow: #f7c600;
    --cream: #f6efe2;
    --charcoal: #333333;
    --ink: #2a2a2a;
    --paper: #ffffff;
    --canvas: #f1f1f1;
    --rule: #9a9a9a;
  }
  html, body {
    margin: 0;
    padding: 0;
    width: 773px;
    height: 1200px;
    overflow: hidden;
    background: var(--canvas);
  }
  .sheet {
    width: 773px;
    height: 1200px;
    display: flex;
    flex-direction: column;
    align-items: center;
    justify-content: center;
    gap: 40px;
  }
  .postcard {
    display: block;
    width: 700px;
    height: 499px;
    background: var(--paper);
    box-shadow: 0 4px 14px rgba(0,0,0,0.22);
  }
  .display { font-family: 'Bebas Neue', 'Oswald', sans-serif; }
  .sans { font-family: 'Montserrat', sans-serif; }
</style>
</head>
<body>
<main class="sheet">

  <!-- Front -->
  <svg class="postcard postcard-front" viewBox="0 0 895 638" xmlns="http://www.w3.org/2000/svg">
    <defs>
      <linearGradient id="houseTones" x1="0" y1="0" x2="0" y2="1">
        <stop offset="0" stop-color="#8e9499"/>
        <stop offset="0.18" stop-color="#e4e7ea"/>
        <stop offset="0.6" stop-color="#cfd3d3"/>
        <stop offset="0.78" stop-color="#8d8a74"/>
        <stop offset="1" stop-color="#a08f7a"/>
      </linearGradient>
      <radialGradient id="dogTones" cx="0.5" cy="0.45" r="0.6">
        <stop offset="0" stop-color="#eceef2"/>
        <stop offset="1" stop-color="#b9bfc9" stop-opacity="0.9"/>
      </radialGradient>
      <clipPath id="frontClip"><rect width="895" height="638"/></clipPath>
    </defs>
    <g clip-path="url(#frontClip)">
      <rect class="front-panel" width="895" height="533" fill="var(--brand-blue)"/>
      <rect class="front-contact-band" y="533" width="895" height="105" fill="var(--charcoal)"/>
      <rect y="529" width="895" height="4" fill="var(--paper)"/>
      <circle class="front-photo" role="img" aria-label="Photo of Wexley the dog sitting in front of a white brick house"
              cx="800" cy="235" r="390" fill="url(#houseTones)" stroke="var(--paper)" stroke-width="4"/>
      <ellipse class="front-dog-cutout" role="img" aria-label="Wexley, a fluffy grey and white dog wearing a bandana"
               cx="579" cy="445" rx="105" ry="168" fill="url(#dogTones)"/>
    </g>

    <text class="sans" x="40" y="53" font-size="30" font-weight="700" fill="var(--paper)" letter-spacing="1">LOGO</text>
    <text class="display" x="38" y="150" font-size="86" fill="var(--cream)">WEXLEY</text>
    <text class="display" x="38" y="305" font-size="197" fill="var(--brand-yellow)">BUYS</text>
    <text class="display" x="38" y="407" font-size="121" fill="var(--paper)">HOUSES</text>

    <g class="price-badge">
      <rect x="42" y="432" width="394" height="72" fill="var(--brand-yellow)"/>
      <rect x="48" y="438" width="382" height="60" fill="none" stroke="var(--charcoal)" stroke-width="1.5"/>
      <text class="display" x="60" y="485" font-size="45" textLength="203" lengthAdjust="spacingAndGlyphs" fill="var(--brand-blue)">PRICE STARTS AT</text>
      <text class="display" x="281" y="464" font-size="22" fill="var(--brand-blue)">$</text>
      <text class="display" x="297" y="487" font-size="52" textLength="123" lengthAdjust="spacingAndGlyphs" fill="var(--brand-blue)">2,50000</text>
    </g>

    <g class="phone-line">
      <path d="M44 548 c3-2 7-2 9 1 l5 8 c1 3 0 5-2 7 l-3 2 c2 5 7 10 12 12 l2-3 c2-2 4-3 7-2 l8 5 c3 2 3 6 1 9 l-3 3 c-4 4-12 3-20-2 c-9-6-16-14-20-23 c-3-7-2-13 1-16z" fill="var(--paper)"/>
      <text class="display" x="89" y="579" font-size="46" textLength="200" lengthAdjust="spacingAndGlyphs" fill="var(--paper)">555-814-2760</text>
    </g>
    <g class="social-handles sans" font-size="13" font-weight="500" fill="var(--paper)">
      <rect x="43" y="592" width="12" height="12" rx="2"/>
      <text x="62" y="603">@WexleyBuysHouses</text>
      <rect x="223" y="592" width="12" height="12" rx="2"/>
      <text x="242" y="603">@WexleyBuysHouses</text>
    </g>
  </svg>

  <!-- Back -->
  <svg class="postcard postcard-back" viewBox="0 0 895 638" xmlns="http://www.w3.org/2000/svg">
    <defs>
      <linearGradient id="houseTonesSmall" x1="0" y1="0" x2="0" y2="1">
        <stop offset="0" stop-color="#8e9499"/>
        <stop offset="0.3" stop-color="#e2e5e8"/>
        <stop offset="0.7" stop-color="#c9cccb"/>
        <stop offset="1" stop-color="#9c8b76"/>
      </linearGradient>
      <radialGradient id="dogTonesBack" cx="0.5" cy="0.45" r="0.6">
        <stop offset="0" stop-color="#eceef2"/>
        <stop offset="1" stop-color="#b9bfc9" stop-opacity="0.9"/>
      </radialGradient>
    </defs>
    <rect width="895" height="638" fill="var(--paper)"/>
    <path class="back-benefits-panel" d="M0 275 C130 350 300 330 400 245 L460 265 L420 533 L0 533 Z" fill="var(--brand-blue)"/>
    <path class="back-contact-band" d="M0 533 L405 533 C415 575 425 610 440 638 L0 638 Z" fill="var(--charcoal)"/>
    <rect y="529" width="420" height="4" fill="var(--paper)"/>
    <circle class="back-photo" role="img" aria-label="Photo of Wexley sitting on the lawn in front of the house"
            cx="455" cy="180" r="80" fill="url(#houseTonesSmall)" stroke="var(--paper)" stroke-width="4"/>
    <ellipse class="back-dog-cutout" role="img" aria-label="Wexley, a fluffy grey and white dog wearing a bandana"
             cx="411" cy="433" rx="85" ry="145" fill="url(#dogTonesBack)"/>

    <g class="brand-title sans" font-size="35" font-weight="800" fill="var(--brand-blue)">
      <text x="38" y="53">WEXLEY BUYS</text>
      <text x="38" y="86">HOUSES</text>
    </g>
    <rect x="41" y="102" width="70" height="5" fill="var(--charcoal)"/>

    <g class="message sans" font-size="21" font-weight="600" fill="var(--ink)">
      <text x="41" y="138">I recently bought a house</text>
      <text x="41" y="164">in (subdivision name) and</text>
      <text x="41" y="190">would love to buy yours</text>
      <text x="41" y="228">Call my humans today so</text>
      <text x="41" y="254">we can give you a no</text>
      <text x="41" y="280">obligation offer</text>
    </g>

    <g class="benefits sans" font-size="20" font-weight="500" fill="var(--paper)">
      <g fill="var(--paper)" stroke="var(--brand-blue)" stroke-width="1.5">
        <circle cx="54" cy="351" r="10"/>
        <circle cx="54" cy="405" r="10"/>
        <circle cx="54" cy="435" r="10"/>
        <circle cx="54" cy="466" r="10"/>
      </g>
      <g fill="none" stroke="var(--brand-blue)" stroke-width="1.5">
        <path d="M49 351 l3 3 l6-6"/>
        <path d="M49 405 l3 3 l6-6"/>
        <path d="M49 435 l3 3 l6-6"/>
        <path d="M49 466 l3 3 l6-6"/>
      </g>
      <text x="77" y="358">No money out of your</text>
      <text x="77" y="381">pocket</text>
      <text x="77" y="411">Quick closing</text>
      <text x="77" y="441">Any condition</text>
      <text x="77" y="472">Can help with moving</text>
      <text x="77" y="495">expenses</text>
    </g>

    <g class="phone-line">
      <path d="M44 548 c3-2 7-2 9 1 l5 8 c1 3 0 5-2 7 l-3 2 c2 5 7 10 12 12 l2-3 c2-2 4-3 7-2 l8 5 c3 2 3 6 1 9 l-3 3 c-4 4-12 3-20-2 c-9-6-16-14-20-23 c-3-7-2-13 1-16z" fill="var(--paper)"/>
      <text class="display" x="89" y="579" font-size="46" textLength="200" lengthAdjust="spacingAndGlyphs" fill="var(--paper)">555-814-2760</text>
    </g>
    <g class="social-handles sans" font-size="13" font-weight="500" fill="var(--paper)">
      <rect x="43" y="592" width="12" height="12" rx="2"/>
      <text x="62" y="603">@WexleyBuysHouses</text>
      <rect x="223" y="592" width="12" height="12" rx="2"/>
      <text x="242" y="603">@WexleyBuysHouses</text>
    </g>

    <text class="sans" x="506" y="59" font-size="30" font-weight="700" fill="var(--ink)" letter-spacing="1">LOGO</text>
    <rect class="stamp-box" x="781" y="38" width="84" height="87" fill="none" stroke="var(--ink)" stroke-width="1.5"/>
    <g class="address-lines" stroke="var(--rule)" stroke-width="1.2">
      <line x1="556" y1="300" x2="866" y2="300"/>
      <line x1="556" y1="343" x2="866" y2="343"/>
      <line x1="556" y1="390" x2="866" y2="390"/>
      <line x1="556" y1="432" x2="866" y2="432"/>
    </g>
  </svg>

</main>
</body>
</html>
```